postcard for Real Estate Agent that sells homes for less than any other agents

My company sells houses for a fraction of what others charge. I have most of the verbiage but I am open to ideas.
Our post card will be 6.25 x 9
We need an image that goes with our words and draws people to take a look
We are playful at the same time very serious about the money we will save our clients. In the past our message has been received as too good to be true. Our old message was "save $6000* when you list with us" We think the "*" was causing people to think their was a catch. Other agents will tell people that we will not do what they will do and that is why they must charge more. We are a full service agency and we will generally do everything that other agents will do and in many cases we will do more than other agents. We are changing this industry and need our message to get to every person that is thinking of selling their home

Target Market(s)

People who want to list their home for sale

Industry/Entity Type

Real Estate Agent

Requirements
Must have
• Image that makes people read the message

```html
<!DOCTYPE html>
<html lang="en">
<head>
<meta charset="utf-8">
<title>Keystone Realty Postcard</title>
<link rel="stylesheet" href="https://fonts.googleapis.com/css2?family=Oswald:wght@400;500;600&family=Roboto+Condensed:wght@400;500&family=Gloria+Hallelujah&family=Roboto:wght@400&display=swap">
<style>
  :root {
    --page: #ffffff;
    --card-edge: #d9d9d9;
    --headline-yellow: #f7e23b;
    --band-lime: #ccf000;
    --alert-red: #e0201a;
    --brand-blue: #23559f;
    --brand-navy: #173a6e;
    --brand-green: #5e8f2c;
    --note-yellow: #f7ec7a;
    --ink: #222222;
  }
  * { box-sizing: border-box; margin: 0; padding: 0; }
  html, body { width: 854px; height: 1200px; overflow: hidden; background: var(--page); }
  .canvas { position: relative; width: 854px; height: 1200px; }

  .card { position: absolute; left: 30px; width: 799px; background: var(--page); border: 1px solid var(--card-edge); overflow: hidden; }
  .card--front { top: 29px; height: 555px; }
  .card--back { top: 613px; height: 562px; }

  /* Front */
  .hero-photo { position: absolute; left: 0; top: 0; width: 799px; height: 289px;
    background: linear-gradient(100deg, #4a5a34 0%, #7d8a5a 30%, #b7b8ad 55%, #9a2b26 72%, #c8c8c4 100%); }
  .hero-copy { position: absolute; left: 0; top: 0; width: 420px; height: 289px; font-family: "Oswald", sans-serif; font-weight: 500; color: var(--headline-yellow); text-shadow: 1px 2px 3px rgba(0,0,0,.75); }
  .hero-copy span { position: absolute; white-space: nowrap; font-weight: 500; }
  .hero-line-1 { left: 28px; top: 136px; font-size: 22px; }
  .hero-line-2 { left: 28px; top: 168px; font-size: 33px; }
  .hero-line-3 { left: 74px; top: 222px; font-size: 24px; }
  .hero-line-4 { left: 117px; top: 256px; font-size: 22px; }

  .ideas-band { position: absolute; left: 0; top: 289px; width: 799px; height: 84px; background: var(--band-lime); text-align: center; }
  .ideas-title { font-family: "Oswald", sans-serif; font-weight: 500; color: var(--alert-red); font-size: 24px; line-height: 34px; }
  .ideas-list { font-family: "Roboto Condensed", sans-serif; font-variant: small-caps; color: var(--brand-blue); font-size: 18px; line-height: 24px; }
  .ideas-list span { margin: 0 6px; }

  .saver-photo { position: absolute; left: 9px; top: 380px; width: 312px; height: 172px;
    background: linear-gradient(120deg, #c89a72 0%, #e9c6b0 45%, #f2a6b8 70%, #f5eee9 100%); }

  .brand { font-family: "Oswald", sans-serif; font-weight: 500; color: var(--brand-blue); display: flex; align-items: center; gap: 8px; white-space: nowrap; }
  .brand-mark { width: 16px; height: 16px; background: var(--brand-green); flex: none; }
  .front-brand { position: absolute; left: 345px; top: 428px; font-size: 26px; }
  .front-contact { position: absolute; left: 560px; top: 410px; width: 220px; text-align: center; font-family: "Oswald", sans-serif; font-weight: 500; color: var(--brand-green); white-space: nowrap; }
  .front-phone { font-size: 30px; line-height: 40px; }
  .front-web { font-size: 20px; line-height: 30px; }
  .front-tagline { position: absolute; left: 365px; top: 512px; font-family: "Oswald", sans-serif; font-weight: 500; font-size: 21px; color: var(--brand-blue); white-space: nowrap; }

  /* Back */
  .back-brand { position: absolute; left: 24px; top: 58px; font-size: 23px; }
  .back-contact { position: absolute; left: 198px; top: 24px; width: 186px; font-family: "Oswald", sans-serif; font-weight: 500; text-align: center; line-height: 28px; white-space: nowrap; }
  .back-contact .call { color: var(--brand-blue); font-size: 19px; }
  .back-contact .phone { color: var(--brand-green); font-size: 21px; }
  .back-contact .web { color: var(--brand-blue); font-size: 18px; }

  .swoosh { position: absolute; left: 392px; top: 0; }
  .return-address { position: absolute; left: 466px; top: 40px; font-family: "Roboto", sans-serif; font-style: normal; font-size: 10px; line-height: 16px; color: var(--ink); }

  .promise-note { position: absolute; left: 50px; top: 150px; width: 322px; height: 300px; background: var(--note-yellow);
    transform: rotate(-2deg); box-shadow: 3px 5px 8px rgba(0,0,0,.25); padding: 28px 20px 0 30px; }
  .promise-title { font-family: "Roboto", sans-serif; font-weight: 400; font-size: 16px; letter-spacing: 1px; color: #5a5a3a; text-align: center; line-height: 22px; text-transform: uppercase; margin-bottom: 10px; }
  .promise-list { list-style: none; font-family: "Gloria Hallelujah", cursive; font-size: 12.5px; line-height: 19px; color: var(--brand-navy); }
  .promise-list li { position: relative; padding-left: 4px; margin-bottom: 6px; }
  .promise-list li::before { content: "\2666"; position: absolute; left: -18px; color: var(--brand-blue); font-size: 10px; }
  .pin { position: absolute; left: 198px; top: 132px; width: 22px; height: 22px; border-radius: 50%; background: #d8261c; }
</style>
</head>
<body>
<div class="canvas">

  <section class="card card--front">
    <div class="hero-photo" role="img" aria-label="Photo of a suburban front yard with a red home for sale sign topped by a sold rider"></div>
    <h1 class="hero-copy">
      <span class="hero-line-1">You'd have to be</span>
      <span class="hero-line-2">Bat $#@T CRAZY</span>
      <span class="hero-line-3">to give an agent $6000</span>
      <span class="hero-line-4">to put a sign in your yard!</span>
    </h1>

    <div class="ideas-band">
      <h2 class="ideas-title">Look at what you can do with $6000</h2>
      <p class="ideas-list">
        <span>Give it to your Kids</span><span>Build a Fence</span><span>Build a Deck</span><span>Landscape</span><span>Take a Vacation</span><span>Buy new</span><br>
        <span>clothes</span><span>Pay off your car</span><span>Pay off Student Loan</span><span>Buy New Carpet</span><span>Upgrade Appliances</span>
      </p>
    </div>

    <div class="saver-photo" role="img" aria-label="Photo of a smiling woman resting her head on a pink piggy bank"></div>
    <div class="brand front-brand"><span class="brand-mark"></span>Keystone Realty</div>
    <div class="front-contact">
      <div class="front-phone">555-014-2278</div>
      <div class="front-web">www.KeystoneRE.example</div>
    </div>
    <p class="front-tagline">Full Service Agency at a Fraction of the Cost!</p>
  </section>

  <section class="card card--back">
    <div class="brand back-brand"><span class="brand-mark"></span>Keystone Realty</div>
    <div class="back-contact">
      <div class="call">Call Dale or Marcus at</div>
      <div class="phone">555-014-2278</div>
      <div class="web">www.KeystoneRE.example</div>
    </div>

    <svg class="swoosh" width="70" height="520" viewBox="0 0 70 520" aria-hidden="true">
      <path d="M14 0 C 42 120, 46 300, 10 510" fill="none" stroke="var(--brand-navy)" stroke-width="6"/>
      <path d="M30 0 C 60 140, 58 320, 20 515" fill="none" stroke="var(--brand-green)" stroke-width="5"/>
    </svg>

    <address class="return-address">
      Keystone Realty Group,<br>LLC<br>4410 Maple Row Avenue<br>Fairview, CO 80000
    </address>

    <div class="promise-note">
      <h3 class="promise-title">Full Service Agency<br>at a Fraction of the Cost</h3>
      <ul class="promise-list">
        <li>We will sell your home FAST</li>
        <li>We will sell your home for the highest possible price</li>
        <li>We will charge you a fraction of what others will charge</li>
        <li>We will save you THOUSANDS of dollars</li>
        <li>If you list your home with anyone else you will lose THOUSANDS of dollars.</li>
      </ul>
    </div>
    <div class="pin" aria-hidden="true"></div>
  </section>

</div>
</body>
</html>
```